Digital Marketing Website Redesign, modern, fresh, dynamic

Hi there, we would like to freshen up our website and create a new dynamic look. We are a digital marketing agency who specialise in digital transformation in the form of creating websites for appointment bookings. Our clients are service businesses such as hairdressers, dentists and doctors who's patients need to book appointments with them.

Our company name is Plombek with the point being we can help increase your revenue curve by increasing your appointment bookings.

Our services include building the website, creating campaigns to drive traffic, increasing conversions and monitoring and reporting.

We are playing with a tagline of 'Step into your Digital Transformation' as we have a 5 step journey that customers can take with us getting them from zero to full appointment bookings.

Our current website is www.plomnbek-site.example

You can see a draft design that I mocked up on Canva here https://www.drawpadhub.example/design/QXT82LmnB7K/PoWz41kdRtGyvb_sxE_JNq/edit?utm_content=QXT82LmnB7K&utm_campaign=designshare&utm_medium=link2&utm_source=sharebutton

Also attached some other homepage ideas. In regard to photos we are open to ideas.

Please let if you need any more information to provide us with an initial design. Thanks million and I look forward to receiving fantastic designs :)

Marissa Tobler
Plombek

Target Market(s)

Appointment based businesses such as hairdressers, dentists, doctors

Industry/Entity Type

Marketing and Digital

Coding

Coded - Design and coding required

Number of Pages Required

1 page

Colors
0094D4
00A9DD
6FCCEA
C7EBF8
E9F6FB

Requirements
Must have
• Appointment booking CTA
Nice to have
• A website we like https://www.morwenhalbrook.example

```html
<!DOCTYPE html>
<html lang="en">
<head>
<meta charset="utf-8">
<title>Plombek – Digital Marketing</title>
<link href="https://fonts.googleapis.com/css2?family=Open+Sans:wght@400;500;600;700&display=swap" rel="stylesheet">
<style>
:root{
  --navy:#203f7c;
  --navy-deep:#162c5c;
  --green:#9caf23;
  --ink:#2c3340;
  --muted:#7b8190;
  --night:#0e1433;
  --light:#f3f5f9;
  --line:#d9dde5;
  --white:#ffffff;
  --orange:#e8791f;
}
*{box-sizing:border-box;margin:0;padding:0}
html,body{width:1200px;height:4726px;overflow:hidden;background:var(--white)}
body{font-family:"Open Sans",sans-serif;color:var(--ink)}
.page{position:relative;width:1200px;height:4726px;overflow:hidden}
.abs{position:absolute}
.photo{position:absolute}
.brand{font-family:"Open Sans",sans-serif;font-weight:700;color:var(--navy);letter-spacing:.5px}
.eyebrow{font-size:13px;font-weight:600;color:var(--green);text-transform:uppercase;letter-spacing:.5px;text-decoration:underline;text-underline-offset:4px}
.section-title{font-size:40px;font-weight:600;color:var(--navy);text-align:center}
.center{left:0;width:1200px;text-align:center}

/* header */
.topbar{left:385px;top:0;width:815px;height:33px;background:var(--navy);display:flex;align-items:center;font-size:11px;font-weight:700;color:var(--white)}
.topbar .item{display:flex;align-items:center;gap:8px;padding:0 28px}
.topbar .cta{background:var(--green);height:33px;padding:0 30px;text-transform:uppercase;font-size:10px}
.header-logo{left:184px;top:38px;font-size:32px}
.nav{left:397px;top:60px;display:flex;gap:26px;font-size:11px;color:var(--ink)}
.contact-btn{left:932px;top:53px;width:118px;height:32px;border:1.5px solid var(--navy);border-radius:3px;font-size:11px;font-weight:600;color:var(--navy);display:flex;align-items:center;justify-content:center}

/* hero */
.hero{left:0;top:101px;width:1200px;height:660px;background:radial-gradient(ellipse at 50% 60%,#2c5a8a 0%,#123459 35%,#0a1a35 70%,#060d1f 100%)}
.hero-tag{left:520px;top:302px;width:160px;height:30px;background:var(--navy);color:var(--white);font-size:11px;font-weight:700;display:flex;align-items:center;justify-content:center}
.hero-title{top:345px;font-size:62px;font-weight:700;color:var(--white);line-height:72px}
.hero-btn{left:517px;top:517px;width:162px;height:46px;border:2px solid var(--white);border-radius:3px;color:var(--white);font-size:12px;font-weight:700;display:flex;align-items:center;justify-content:center}
.swoosh{left:0;top:600px}

/* about */
.logo-badge{left:298px;top:988px;width:102px;height:102px;border-radius:50%;background:var(--white);display:flex;align-items:center;justify-content:center;font-size:18px;box-shadow:0 2px 8px rgba(0,0,0,.15)}
.about-text{left:624px;top:835px;width:500px}
.about-text h2{font-size:40px;font-weight:600;color:var(--navy);line-height:53px;margin-top:18px}
.about-text h3{font-size:22px;font-weight:500;color:var(--navy);margin-top:22px}
.about-text p{font-size:12.5px;line-height:19px;color:var(--muted);margin-top:14px}
.btn-green{background:var(--green);color:var(--white);font-weight:600;display:inline-flex;align-items:center;justify-content:center;gap:10px;border-radius:2px}
.about-text .btn-green{width:152px;height:44px;font-size:14px;margin-top:26px}

/* services */
.services{left:0;top:1317px;width:1200px;height:652px;background:var(--light)}
.svc-card{position:absolute;top:1596px;width:325px;height:309px}
.svc-card .img{position:absolute;left:0;top:0;width:325px;height:261px}
.svc-card .icon{position:absolute;left:116px;top:-50px;width:94px;height:94px;border-radius:50%;border:2px solid var(--green);border-bottom-color:transparent;border-left-color:transparent;border-right-color:transparent;display:flex;align-items:center;justify-content:center}
.svc-card .icon span{width:80px;height:80px;border-radius:50%;background:var(--navy);display:flex;align-items:center;justify-content:center}
.svc-card .label{position:absolute;left:26px;top:215px;width:273px;height:94px;background:var(--white);display:flex;align-items:center;justify-content:center;font-size:19px;color:var(--navy);box-shadow:0 4px 10px rgba(0,0,0,.06)}

/* band */
.band{left:0;top:1969px;width:1200px;height:307px;background:radial-gradient(ellipse at 70% 40%,#3d2a6e 0%,#1d1a4a 45%,#0c1030 100%)}
.band-title{top:2078px;font-size:34px;font-weight:500;color:var(--white);line-height:43px}
.contact-pill{left:350px;top:2246px;width:501px;height:51px;background:var(--white);border-radius:3px;display:flex;align-items:center;justify-content:space-around;font-size:16px;color:var(--ink);box-shadow:0 4px 12px rgba(0,0,0,.08);z-index:5}

/* why */
.why{left:0;top:2276px;width:1200px;height:792px;background:linear-gradient(90deg,#eef1f6 0%,#e6eaf1 45%,#cfd8e4 70%,#b9c6d6 100%)}
.why-card{position:absolute;width:235px;height:262px;background:var(--white);text-align:center;padding-top:32px}
.why-card .ic{width:86px;height:86px;border-radius:50%;background:#eef0f4;margin:0 auto;display:flex;align-items:center;justify-content:center}
.why-card h4{font-size:21px;font-weight:500;color:var(--navy);margin-top:24px}
.why-card p{font-size:12.5px;line-height:18px;color:var(--muted);margin:14px 20px 0}
.why-card.active{background:var(--navy)}
.why-card.active .ic{background:var(--white)}
.why-card.active h4,.why-card.active p{color:var(--white)}

/* reviews */
.reviews-bg{left:0;top:3068px;width:1200px;height:358px;background:linear-gradient(180deg,#1b2433 0%,#243247 50%,#1a2230 100%)}
.review{position:absolute;top:3307px;width:301px;height:326px;background:var(--white);box-shadow:0 4px 16px rgba(0,0,0,.08);padding:44px 36px 0 42px}
.review .quote{position:absolute;left:-24px;top:40px;width:52px;height:52px;border-radius:50%;background:var(--green);color:var(--white);font-size:40px;font-weight:700;display:flex;align-items:center;justify-content:center;line-height:1}
.review .stars{color:var(--orange);font-size:15px;letter-spacing:8px}
.review p{font-size:13px;line-height:19px;color:var(--muted);margin-top:14px}
.review hr{border:none;border-top:1px solid #9aa0ab;margin-top:30px}
.review .who{display:flex;align-items:center;gap:14px;margin-top:26px}
.review .av{width:58px;height:58px;border-radius:50%;background:linear-gradient(135deg,#e9d3c3,#b98a6e)}
.review .name{font-size:15px;color:var(--ink)}
.review .city{font-size:13px;color:var(--muted);margin-top:4px}

/* contact */
.footer-bg{left:0;top:4202px;width:1200px;height:524px;background:radial-gradient(ellipse at 15% 30%,#1a3a63 0%,#0f1f3f 40%,#0b1330 100%)}
.form-card{left:138px;top:3868px;width:923px;height:457px;background:var(--white);border-radius:14px;overflow:hidden;box-shadow:0 6px 20px rgba(0,0,0,.1)}
.form-photo{left:0;top:0;width:462px;height:457px;background:linear-gradient(135deg,#f2f0ec 0%,#ddd6cc 60%,#b7a590 100%)}
.form-logo{left:515px;top:40px;font-size:36px}
.form-title{left:511px;top:108px;font-size:28px;color:var(--navy);font-weight:400}
.field{position:absolute;border:1px solid #c8ccd4;border-radius:2px;font-size:11px;color:var(--muted);padding:8px 8px}
.send{left:512px;top:362px;width:357px;height:36px;font-size:13px}

/* footer */
.footer-logo{top:4392px;font-size:48px;color:#3f74b8}
.footer-nav{left:0;width:1200px;top:4487px;display:flex;justify-content:center;gap:46px;font-size:14px;font-weight:500;color:var(--white);padding-right:30px}
.footer-rule{left:140px;top:4538px;width:920px;height:1px;background:rgba(255,255,255,.25)}
.f-item{position:absolute;top:4580px;display:flex;align-items:center;gap:18px;color:var(--white);font-size:12px;line-height:17px}
.f-item .circ{width:56px;height:56px;border-radius:50%;border:1.5px solid rgba(255,255,255,.6);display:flex;align-items:center;justify-content:center}
.f-item b{font-weight:600;font-size:13px}
.f-div{position:absolute;top:4575px;width:1px;height:66px;background:rgba(255,255,255,.45)}
.bottom-bar{left:0;top:4668px;width:1200px;height:58px;background:var(--green);display:flex;align-items:center;justify-content:space-between;padding:0 146px;color:var(--white);font-size:12px;font-weight:600}
.socials{display:flex;gap:8px}
.socials span{width:26px;height:26px;border:1.5px solid var(--white);border-radius:3px}
</style>
</head>
<body>
<div class="page">

  <!-- header -->
  <div class="abs topbar">
    <div class="item">
      <svg width="12" height="12" viewBox="0 0 24 24" fill="none" stroke="#fff" stroke-width="2"><path d="M5 3h4l2 5-3 2a11 11 0 0 0 6 6l2-3 5 2v4a2 2 0 0 1-2 2A18 18 0 0 1 3 5a2 2 0 0 1 2-2z"/></svg>
      555 - 014 - 2280
    </div>
    <div class="item cta">
      <svg width="14" height="11" viewBox="0 0 24 18" fill="none" stroke="#fff" stroke-width="2"><rect x="1" y="1" width="22" height="16"/><path d="M1 1l11 9 11-9"/></svg>
      Request an appointment
    </div>
    <div class="item">
      <svg width="11" height="13" viewBox="0 0 20 24" fill="none" stroke="#fff" stroke-width="2"><path d="M10 23s8-8 8-13a8 8 0 0 0-16 0c0 5 8 13 8 13z"/><circle cx="10" cy="10" r="3"/></svg>
      48 Larkfield Row Eastvale
    </div>
  </div>
  <div class="abs brand header-logo">Plombek</div>
  <nav class="abs nav"><span>THUIS</span><span>Behandelingenvergoeding</span><span>Ons team</span><span>Folders</span></nav>
  <div class="abs contact-btn">CONTACT US</div>

  <!-- hero -->
  <div class="photo hero" role="img" aria-label="Person walking through a glowing digital data tunnel"></div>
  <div class="abs hero-tag">DIGITAL MARKETING</div>
  <h1 class="abs center hero-title">Elevate Your Brand,<br>Dominate the Digital Scene</h1>
  <div class="abs hero-btn">LEARN MORE</div>
  <svg class="abs swoosh" width="1200" height="170" viewBox="0 0 1200 170">
    <path d="M0 60 C300 150 700 150 1200 30 L1200 170 L0 170Z" fill="#fff"/>
    <path d="M0 60 C300 150 700 150 1200 30 L1200 55 C720 165 300 165 0 70Z" fill="#203f7c"/>
    <path d="M300 120 C650 150 900 90 1200 20 L1200 32 C900 104 650 150 300 120Z" fill="#9caf23"/>
  </svg>

  <!-- about -->
  <div class="photo" style="left:90px;top:857px;width:246px;height:363px;background:linear-gradient(135deg,#d7dde4 0%,#9aa5b1 55%,#4d5560 100%)" role="img" aria-label="Man with glasses pointing at a computer screen"></div>
  <div class="photo" style="left:350px;top:838px;width:226px;height:195px;background:linear-gradient(135deg,#8a97a8 0%,#3f4c5e 60%,#1f2a3a 100%)" role="img" aria-label="Hands on a laptop with floating digital marketing icons"></div>
  <div class="photo" style="left:350px;top:1046px;width:226px;height:220px;background:linear-gradient(135deg,#3a4f7a 0%,#1e2a4d 55%,#b0506a 100%)" role="img" aria-label="Woman with headset working at a computer"></div>
  <div class="abs brand logo-badge">Plombek</div>
  <div class="abs about-text">
    <div class="eyebrow">About us</div>
    <h2>Fueling Growth in<br>the Digital Fast Lane</h2>
    <h3>Online Presence, Unleashed Potential</h3>
    <p>Lorem ipsum dolor sit amet, consectetur adipiscing elit, sed do eiusmod tempor incididunt ut labore et dolore magna aliqua. Ut enim ad minim veniam, quis nostrud exercitation ullamco laboris nisi ut aliquip ex ea commodo consequat. Duis aute irure dolor in reprehenderit in voluptate velit esse cillum dolore eu fugiat nulla pariatur. Excepteur sint occaecat cupidatat non proident, sunt in culpa qui officia deserunt mollit anim id est laborum.</p>
    <div class="btn-green">Learn More
      <svg width="16" height="12" viewBox="0 0 16 12" fill="none" stroke="#fff" stroke-width="1.8"><path d="M1 6h13M9 1l5 5-5 5"/></svg>
    </div>
  </div>

  <!-- services -->
  <div class="abs services"></div>
  <div class="abs center" style="top:1396px"><span class="eyebrow" style="text-transform:none;font-size:12px">Our Services</span></div>
  <h2 class="abs center section-title" style="top:1432px">Our Services</h2>

  <div class="svc-card" style="left:90px">
    <div class="img" style="background:linear-gradient(135deg,#4b5a6e 0%,#1d2838 60%,#0d141f 100%)" role="img" aria-label="Hand touching a digital marketing interface"></div>
    <div class="icon"><span><svg width="34" height="34" viewBox="0 0 34 34" fill="#fff"><circle cx="17" cy="4" r="3"/><circle cx="26" cy="8" r="2.6"/><circle cx="30" cy="17" r="2.3"/><circle cx="26" cy="26" r="2"/><circle cx="17" cy="30" r="1.8"/><circle cx="8" cy="26" r="1.6"/><circle cx="4" cy="17" r="1.4"/><circle cx="8" cy="8" r="1.2"/></svg></span></div>
    <div class="label">Marketing Services</div>
  </div>
  <div class="svc-card" style="left:440px">
    <div class="img" style="background:linear-gradient(135deg,#5d7a95 0%,#2e4661 55%,#b0405a 100%)" role="img" aria-label="Person using a laptop with online booking graphics"></div>
    <div class="icon"><span><svg width="30" height="34" viewBox="0 0 30 34" fill="none" stroke="#fff" stroke-width="2.2" stroke-linecap="round"><path d="M12 18V6a3 3 0 0 1 6 0v9l7 2a3 3 0 0 1 2 3l-1 8a4 4 0 0 1-4 4h-7a4 4 0 0 1-3-2l-5-7a2.5 2.5 0 0 1 4-3l1 1"/></svg></span></div>
    <div class="label">Online Booking Apps</div>
  </div>
  <div class="svc-card" style="left:791px">
    <div class="img" style="background:linear-gradient(135deg,#e2e6ea 0%,#b8c1cb 55%,#7d8896 100%)" role="img" aria-label="Team meeting around a table with charts"></div>
    <div class="icon"><span><svg width="34" height="34" viewBox="0 0 34 34" fill="#fff"><path d="M17 3l4 5h-3v6h-2V8h-3z"/><path d="M17 31l-4-5h3v-6h2v6h3z"/><path d="M3 17l5-4v3h6v2H8v3z"/><path d="M31 17l-5 4v-3h-6v-2h6v-3z"/></svg></span></div>
    <div class="label">Services Marketing</div>
  </div>

  <!-- availability band -->
  <div class="photo band" role="img" aria-label="Abstract purple network of glowing connection lines"></div>
  <div class="abs center band-title">We are available 24/7 to cater for your<br>digital marketing needs</div>

  <!-- why choose us -->
  <div class="photo why" role="img" aria-label="Smiling businesswoman with crossed arms in a bright office"></div>
  <div class="abs contact-pill"><span>+ (001) 555-018-442</span><span>[or]</span><span>hello@plombek.example</span></div>
  <div class="abs center" style="top:2334px"><span class="eyebrow" style="font-size:11px">Why Choose Us</span></div>
  <h2 class="abs center section-title" style="top:2370px">Why Choose Us</h2>

  <div class="why-card" style="left:97px;top:2470px">
    <div class="ic"><svg width="40" height="40" viewBox="0 0 40 40" fill="none" stroke="#9caf23" stroke-width="3"><path d="M8 22a12 12 0 0 1 24 0"/><rect x="10" y="20" width="20" height="12" rx="3"/><path d="M15 26h10"/></svg></div>
    <h4>Quality Services</h4>
    <p>Lorem ipsum dolor sit amet, consectetur adipiscing elit, sed do eiusmod tem</p>
  </div>
  <div class="why-card active" style="left:354px;top:2470px">
    <div class="ic"><svg width="44" height="44" viewBox="0 0 44 44" fill="none" stroke="#9caf23" stroke-width="3.5"><circle cx="22" cy="22" r="17"/><circle cx="22" cy="22" r="9"/></svg></div>
    <h4>Expertise</h4>
    <p>Lorem ipsum dolor sit amet, consectetur adipiscing elit, sed do eiusmod tem</p>
  </div>
  <div class="why-card" style="left:609px;top:2470px">
    <div class="ic"><svg width="40" height="40" viewBox="0 0 40 40" fill="none" stroke="#9caf23" stroke-width="3" stroke-linecap="round"><circle cx="20" cy="9" r="4"/><path d="M8 17h24M20 17v8M20 25l-7 9M20 25l7 9"/></svg></div>
    <h4>Client-centric</h4>
    <p>Lorem ipsum dolor sit amet, consectetur adipiscing elit, sed do eiusmod tem</p>
  </div>
  <div class="why-card" style="left:97px;top:2754px">
    <div class="ic"><svg width="42" height="40" viewBox="0 0 42 40" fill="none" stroke="#9caf23" stroke-width="3" stroke-linecap="round"><circle cx="13" cy="13" r="5"/><path d="M4 30a9 9 0 0 1 18 0M26 14h12M26 21h12M26 28h8"/></svg></div>
    <h4>Personalized</h4>
    <p>Lorem ipsum dolor sit amet, consectetur adipiscing elit, sed do eiusmod tem</p>
  </div>
  <div class="why-card" style="left:354px;top:2754px">
    <div class="ic"><svg width="40" height="40" viewBox="0 0 40 40" fill="#9caf23"><rect x="5" y="26" width="5" height="9"/><rect x="13" y="20" width="5" height="15"/><rect x="21" y="14" width="5" height="21"/><circle cx="31" cy="8" r="3"/><rect x="29" y="13" width="5" height="22"/></svg></div>
    <h4>Professional</h4>
    <p>Lorem ipsum dolor sit amet, consectetur adipiscing elit, sed do eiusmod tem</p>
  </div>
  <div class="why-card" style="left:609px;top:2754px">
    <div class="ic"><svg width="40" height="40" viewBox="0 0 40 40" fill="none" stroke="#9caf23" stroke-width="3"><rect x="5" y="5" width="9" height="9"/><rect x="26" y="5" width="9" height="9"/><rect x="5" y="26" width="9" height="9"/><rect x="26" y="26" width="9" height="9"/><path d="M14 9h12M30 14v12M14 30h12"/></svg></div>
    <h4>Proven Record</h4>
    <p>Lorem ipsum dolor sit amet, consectetur adipiscing elit, sed do eiusmod tem</p>
  </div>

  <!-- reviews -->
  <div class="photo reviews-bg" role="img" aria-label="Developers working at screens full of code"></div>
  <div class="abs center" style="top:3160px;font-size:12px;font-weight:600;color:#fff;text-decoration:underline;text-underline-offset:4px">TESTIMONIALS</div>
  <h2 class="abs center section-title" style="top:3194px;color:#fff">Client Reviews</h2>

  <div class="review" style="left:110px">
    <div class="quote">&ldquo;</div>
    <div class="stars">★★★★★</div>
    <p>Lorem ipsum dolor sit amet, consectetur adipiscing elit, sed do eiusmod tempor incididunt ut labore et dolore magna aliqua. Ut enim ad minim veniam, q</p>
    <hr>
    <div class="who"><div class="av" role="img" aria-label="Client portrait"></div><div><div class="name">Tomas Wendrick</div><div class="city">Lindhaven</div></div></div>
  </div>
  <div class="review" style="left:461px">
    <div class="quote">&ldquo;</div>
    <div class="stars">★★★★★</div>
    <p>Lorem ipsum dolor sit amet, consectetur adipiscing elit, sed do eiusmod tempor incididunt ut labore et dolore magna aliqua. Ut enim ad minim veniam, q</p>
    <hr>
    <div class="who"><div class="av" role="img" aria-label="Client portrait"></div><div><div class="name">Tomas Wendrick</div><div class="city">Lindhaven</div></div></div>
  </div>
  <div class="review" style="left:806px">
    <div class="quote">&ldquo;</div>
    <div class="stars">★★★★★</div>
    <p>Lorem ipsum dolor sit amet, consectetur adipiscing elit, sed do eiusmod tempor incididunt ut labore et dolore magna aliqua. Ut enim ad minim veniam, q</p>
    <hr>
    <div class="who"><div class="av" role="img" aria-label="Client portrait"></div><div><div class="name">Tomas Wendrick</div><div class="city">Lindhaven</div></div></div>
  </div>

  <!-- contact -->
  <div class="abs center" style="top:3714px"><span class="eyebrow" style="font-size:12px">Contact us</span></div>
  <h2 class="abs center section-title" style="top:3748px">Get in touch with us</h2>

  <div class="photo footer-bg" role="img" aria-label="Dark blue abstract digital particle landscape"></div>
  <div class="abs form-card">
    <div class="photo form-photo" role="img" aria-label="Smiling woman holding a tablet in an office"></div>
    <div class="abs brand form-logo">Plombek</div>
    <div class="abs form-title">Please fill out the form</div>
    <div class="field" style="left:512px;top:171px;width:357px;height:37px">Name</div>
    <div class="field" style="left:512px;top:224px;width:171px;height:37px">Phone</div>
    <div class="field" style="left:698px;top:224px;width:171px;height:37px">Email</div>
    <div class="field" style="left:512px;top:275px;width:357px;height:70px">Message</div>
    <div class="abs btn-green send">Send</div>
  </div>

  <!-- footer -->
  <div class="abs center brand footer-logo">Plombek</div>
  <nav class="abs footer-nav"><span>HOME</span><span>SERVICES</span><span>ABOUT US</span><span>TESTIMONIALS</span><span>BLOG</span></nav>
  <div class="abs footer-rule"></div>

  <div class="f-item" style="left:172px">
    <div class="circ"><svg width="28" height="28" viewBox="0 0 28 28" fill="none" stroke="#fff" stroke-width="1.6"><circle cx="14" cy="14" r="12"/><ellipse cx="14" cy="14" rx="5" ry="12"/><path d="M2 14h24M4 8h20M4 20h20"/></svg></div>
    <div>27, Harbour Court, Quay Lane<br>Dunmere, State QZ 480215</div>
  </div>
  <div class="f-div" style="left:430px"></div>
  <div class="f-item" style="left:505px">
    <div class="circ"><svg width="22" height="28" viewBox="0 0 22 28" fill="none" stroke="#fff" stroke-width="1.8"><rect x="3" y="2" width="16" height="24" rx="3"/><path d="M9 22h4"/></svg></div>
    <div><b>PHONE</b><br>(555) 019 3374</div>
  </div>
  <div class="f-div" style="left:750px"></div>
  <div class="f-item" style="left:826px">
    <div class="circ"><svg width="28" height="22" viewBox="0 0 28 22" fill="none" stroke="#fff" stroke-width="1.8"><rect x="2" y="2" width="24" height="18"/><path d="M2 2l12 10 12-10"/></svg></div>
    <div><b>EMAIL</b><br>info@plombek.example</div>
  </div>

  <div class="abs bottom-bar"><span>Plombek</span><div class="socials"><span></span><span></span><span></span><span></span></div></div>
</div>
</body>
</html>
```